Brisk Hounds Dog Behaviour, Training and Natural Healthcare Business Card Design

I am an experienced and qualified dog behavioural trainer and natural animal healthcare consultant offering a range of services to help pet dog owners with the "whole dog".
COLOURS: A soft light blue in the background - can be fading out or split, red should also feature
LOGO: Dog, healing hands, silhouette, shadow
SERVICES: Behaviour Consults, Training, Complex Skills Coaching Walking Coaching, Diet & Nutrition, Environmental Enrichment, Lifestyle and Lifestage Adaptations, Massage, Natural Health Options
BY LINE: Happy Dogs, Happy Owners
VALUES: Promoting communication and connection between dogs and their owners.
FOCUS: Nutritional guidance and environmental adaptation are often needed to complete the package and increase the success rate of training and behaviour modification.

Target Market(s)

Everyone who has a dog who they wish to improve their relationship with

Industry/Entity Type

Communication

Contact Information for Business Card

Brisk Hounds, Renata Walcott, 0472 680351, briskhounds7@mailnest.example, www.briskhounds7.example, Qualified Dog Behavioural Trainer and Natural Animal Healthcare Consultant

Font styles to use
Sans Serif
Script

Colors
85cae6
ec2027

Requirements
Must have
• A clear indication that it is a dog services business. A raised feature
Should not have
• Pawprints, cartoons

```html
<!DOCTYPE html>
<html lang="en">
<head>
<meta charset="utf-8">
<title>Brisk Hounds — Business Card</title>
<link rel="stylesheet" href="https://fonts.googleapis.com/css2?family=Krona+One&family=Pathway+Gothic+One&family=Oswald:wght@400;500&display=swap">
<style>
  :root {
    --card-bg: #f0eff0;
    --sky-blue: #85cae6;
    --sky-blue-soft: #cfe9f4;
    --accent-red: #ec2027;
    --name-slate: #4a586b;
    --tagline-ink: #2e2e30;
    --contact-ink: #3f4a56;
    --badge-bg: #ffffff;
    --badge-letter: #4a586b;
  }
  html, body {
    margin: 0;
    padding: 0;
    overflow: hidden;
    background: var(--card-bg);
  }
  .card {
    position: relative;
    width: 1200px;
    height: 720px;
    background: linear-gradient(180deg, var(--card-bg) 0%, var(--card-bg) 55%, var(--sky-blue-soft) 100%);
    overflow: hidden;
  }
  .byline {
    position: absolute;
    left: 0;
    width: 1200px;
    top: 128px;
    margin: 0;
    text-align: center;
    font-family: "Oswald", sans-serif;
    font-weight: 500;
    font-size: 20px;
    line-height: 28px;
    letter-spacing: 4px;
    text-transform: uppercase;
    color: var(--accent-red);
  }
  .brand-mark {
    position: absolute;
    left: 523px;
    top: 190px;
    width: 160px;
    height: 160px;
    border-radius: 50%;
    background: var(--sky-blue);
  }
  .brand-name {
    position: absolute;
    left: 0;
    width: 1200px;
    top: 398px;
    margin: 0;
    text-align: center;
    font-family: "Krona One", sans-serif;
    font-weight: 400;
    font-size: 50px;
    line-height: 72px;
    letter-spacing: 4px;
    color: var(--name-slate);
  }
  .tagline {
    position: absolute;
    left: 0;
    width: 1200px;
    top: 490px;
    margin: 0;
    text-align: center;
    font-family: "Pathway Gothic One", sans-serif;
    font-size: 35px;
    line-height: 46px;
    color: var(--tagline-ink);
  }
  .consultant {
    position: absolute;
    left: 0;
    width: 1200px;
    top: 552px;
    margin: 0;
    text-align: center;
    font-family: "Oswald", sans-serif;
    font-size: 17px;
    line-height: 26px;
    letter-spacing: 1px;
    color: var(--contact-ink);
  }
  .consultant-name {
    font-weight: 500;
    color: var(--accent-red);
  }
  .contact-band {
    position: absolute;
    left: 0;
    top: 618px;
    width: 1200px;
    height: 102px;
    background: var(--sky-blue);
  }
  .contacts {
    position: absolute;
    top: 650px;
    left: 0;
    width: 1200px;
    height: 38px;
  }
  .contact {
    position: absolute;
    top: 0;
    display: flex;
    align-items: center;
    gap: 14px;
    height: 38px;
  }
  .contact--email { left: 126px; }
  .contact--phone { left: 555px; }
  .contact--web   { left: 871px; }
  .contact-badge {
    width: 38px;
    height: 38px;
    border-radius: 50%;
    background: var(--badge-bg);
    color: var(--badge-letter);
    font-family: "Oswald", sans-serif;
    font-size: 22px;
    line-height: 38px;
    text-align: center;
  }
  .contact-text {
    font-family: "Oswald", sans-serif;
    font-size: 16px;
    letter-spacing: 1px;
    color: var(--contact-ink);
  }
</style>
</head>
<body>
  <main class="card">
    <p class="byline">Happy Dogs, Happy Owners</p>
    <div class="brand-mark" aria-hidden="true"></div>
    <h1 class="brand-name">Brisk Hounds</h1>
    <p class="tagline">Dog Behaviour, Training and Natural Health Care</p>
    <p class="consultant"><span class="consultant-name">Renata Walcott</span> · Qualified Dog Behavioural Trainer and Natural Animal Healthcare Consultant</p>
    <div class="contact-band" aria-hidden="true"></div>
    <div class="contacts">
      <div class="contact contact--email">
        <span class="contact-badge">E</span>
        <span class="contact-text">briskhounds7@mailnest.example</span>
      </div>
      <div class="contact contact--phone">
        <span class="contact-badge">T</span>
        <span class="contact-text">047-268-0351</span>
      </div>
      <div class="contact contact--web">
        <span class="contact-badge">W</span>
        <span class="contact-text">www.briskhounds7.example</span>
      </div>
    </div>
  </main>
</body>
</html>
```